Webdesign für Raumgestalter / Interior Designer und Implementierung
Zielgruppe
Wir möchten zukünftig für Menschen «Träume in Räume» verwandeln und sind spezialisiert auf Interior Design, ReDesign Home Staging wie auch Dekorationen mit folgenden Leistungen an:
- Interior Design
- Home Styling
- Home Staging
- Dekoration
Aufgabenstellung
(Wichtig: Bitte Anforderungen und Fotos im PDF File im Anhang beachten)
Aufbau der Homepage
Homepage wird in verschiedenen Seiten/Fenster aufgebaut. Diese können oben auf der Homepage angeklickt werden. Der Aufbau ist in 5 Seiten: Home, Leistungen, Referenzen, Pakete und Preise, Kontakt
- Die Homepage sollte dann von uns gemanagt werden können. (Bspw. Plattformen oder andere Gremien, wo die Homepage einfach und ohne tiefe Informatikkenntnisse gemanagt werden kann :-).)
- Die Leistungen betreffen Templating inkl. Umsetzung (Online-Fertigstellung), ich kann bei der URL-Verknüpfung unterstützen.
1) Home
Willkommensseite, inspirierend, einladend, sollte die Besucher dazu animieren vertiefter die Detail anzuschauen.
Es soll ein Button unten ermöglichen, ins zweite Fenster «Referenzen» zu klicken. Siehe unteres Kapitel.
2) Leistungen
a. Interior Design
b. Home Styling
c. Home Staging
d. Dekoration
Hier wird der Ablauf von Projekten aufgezeigt, dieser bildet sich in:
- Planung, Designen, Realisieren
Weiterer sollen realisierte Design-Projekte von bspw. Räumen mit Fotos aufgeführt sein.
3) Referenzen
- Dieses Fenster soll das Interesse möglicher Kunden im Detail erwecken
- Es soll ein erster Termin telefonisch oder per Videocall stattfinden können
(dient zum Kennenlernen, Bedürfnisse verstehen, Ablauf aufzeigen)
4) Pakete und Preise
Hier werden die Pakete und Preise beschrieben.
Die Preise werden auf Rapportsbasis erstellt und richten sich nach Offerten und Wünschen des Kunden. Preis ist bei 80 Franken pro Stunde, das erste Beratungsgespräch wird nicht verrechnet.
Hier können Details in einer Tabelle / Preisliste erarbeitet werden:
- Private Wohnräume
o Private Wohnung
o Privates Haus
o Ferienimmobilien
- Business Einrichtungen
o Einrichtungen von Geschäften
o NestoFlat-Einrichtungen
o ReDesign für Verkauf von Immo..

```html
<!DOCTYPE html>
<html lang="de">
<head>
<meta charset="utf-8">
<title>Raumklang – Interior-Konzepte</title>
<link href="https://fonts.googleapis.com/css2?family=Poppins:wght@400;500;600&family=Roboto:wght@400;500;700&display=swap" rel="stylesheet">
<style>
:root{
  --nav:#333333;
  --ink:#222222;
  --text:#333333;
  --white:#ffffff;
  --grey:#b3b3b3;
  --grey-dark:#444444;
  --green-deep:#2c3f38;
  --green-mid:#4a5e50;
  --teal:#1b6f7a;
}
*{margin:0;padding:0;box-sizing:border-box}
html,body{width:1200px;height:2849px;overflow:hidden;background:var(--white)}
body{position:relative;font-family:'Roboto',sans-serif;color:var(--text)}
.abs{position:absolute}
.center{left:0;width:1200px;text-align:center}

.topbar{top:0;left:0;width:1200px;height:54px;background:var(--nav)}
.brand{left:28px;top:12px;width:53px;height:31px;background:var(--white);display:flex;align-items:center;justify-content:center;font-family:'Poppins',sans-serif;font-size:8px;color:var(--grey-dark)}
.nav-link{top:19px;font-size:12px;color:var(--white)}
.nav-link.active{border-bottom:1px solid var(--white);padding-bottom:3px}
.nav-cta{left:1079px;top:13px;width:84px;height:27px;background:var(--grey);color:var(--white);font-size:12px;border-radius:3px;display:flex;align-items:center;justify-content:center}

.hero{top:77px;left:0;width:1200px;height:567px;background:linear-gradient(180deg,#5a6a62 0%,#4c5d52 45%,#33473b 80%,#2b3b31 100%)}
.hero-title{top:362px;font-family:'Poppins',sans-serif;font-weight:500;font-size:27px;color:rgba(255,255,255,.78)}
.hero-sub{top:413px;font-size:13px;color:var(--white)}

.intro-title{top:701px;font-family:'Poppins',sans-serif;font-weight:500;font-size:18px;color:var(--ink)}
.intro-p{font-size:13px;line-height:20px;color:var(--ink)}
.intro-p b{font-weight:700}

.focus{top:952px;left:0;width:1200px;height:481px;background:radial-gradient(ellipse at 50% 55%,#5d6e62 0%,#3e5247 50%,#2a3b33 100%)}
.focus-frame{top:1039px;left:351px;width:498px;height:306px;border:2px solid var(--white)}
.focus-title{top:1098px;font-family:'Poppins',sans-serif;font-weight:500;font-size:34px;color:var(--white)}
.focus-sub{top:1158px;font-family:'Poppins',sans-serif;font-weight:500;font-size:17px;color:var(--white)}
.focus-text{top:1195px;font-size:13px;line-height:20px;color:var(--white)}
.btn-light{left:549px;top:1257px;width:102px;height:35px;background:var(--white);color:var(--ink);font-size:12px;border-radius:3px;display:flex;align-items:center;justify-content:center}

.about-title{left:129px;top:1488px;font-family:'Poppins',sans-serif;font-weight:500;font-size:27px;color:var(--ink)}
.photo{top:1661px;width:460px;height:464px}
.photo-portrait{left:129px;background:linear-gradient(160deg,#3d5a38 0%,#5b4a33 50%,#d8cfc4 100%)}
.photo-room{left:611px;background:linear-gradient(170deg,#ece6dd 0%,#e3d9cb 60%,#6f8a4c 100%)}
.card-title{top:2139px;font-family:'Poppins',sans-serif;font-weight:500;font-size:18px;color:var(--ink)}
.card-text{top:2177px;width:462px;font-size:13px;line-height:20px;color:var(--ink)}

.cta{top:2287px;left:0;width:1200px;height:274px;background:var(--grey)}
.cta-title{top:2342px;font-family:'Poppins',sans-serif;font-weight:500;font-size:25px;color:var(--white)}
.cta-text{top:2406px;font-size:13px;line-height:20px;color:var(--white)}
.btn-outline{left:548px;top:2476px;width:104px;height:35px;border:1px solid var(--grey-dark);border-radius:3px;color:var(--white);font-size:12px;display:flex;align-items:center;justify-content:center}

.footer{top:2561px;left:0;width:1200px;height:188px;background:var(--nav)}
.footer-line{font-size:12px;color:var(--white)}
.footer-line a{color:var(--white);text-decoration:underline}
.footer-line span.sep{margin:0 10px}
.footer-links a{margin:0 6px}

.builder{top:2792px;font-size:10px;color:var(--ink)}
.builder-name{font-family:'Poppins',sans-serif;font-weight:600;font-size:13px;color:var(--teal);margin-right:6px;vertical-align:-1px}
.builder a{color:var(--ink)}
</style>
</head>
<body>

<header class="abs topbar"></header>
<div class="abs brand">Raumklang</div>
<a class="abs nav-link active" style="left:401px">Home</a>
<a class="abs nav-link" style="left:461px">Leistungen</a>
<a class="abs nav-link" style="left:545px">Referenzen</a>
<a class="abs nav-link" style="left:631px">Pakete und Preise</a>
<a class="abs nav-link" style="left:750px">Kontakt</a>
<a class="abs nav-cta">Kontakt</a>

<section class="abs hero" role="img" aria-label="Gewächshaus mit Glastür und grünen Palmpflanzen"></section>
<h1 class="abs center hero-title">Interior-Konzepte für jedes Bedürfnis</h1>
<p class="abs center hero-sub">Home Styling - Home Staging - Dekorationen - Interior Design</p>
<svg class="abs" style="left:594px;top:617px" width="12" height="7" viewBox="0 0 12 7"><path d="M0 0h12L6 7z" fill="#ffffff"/></svg>

<h2 class="abs center intro-title">Wir verwandeln Träume in Räume</h2>
<p class="abs center intro-p" style="top:753px">Möchten Sie Ihre Wohnung dekorieren? Oder ein neues Konzept erstellen lassen?</p>
<p class="abs center intro-p" style="top:793px">Durch jahrelange Erfahrung in <b>Dekoration</b> und <b>Visual Merchandising</b>, wie auch einem<br>Studium in <b>Design</b>, helfe ich Ihnen zu neuen <b>Dekorationen und Konzepten mit<br>persönlichem Charakter</b>.</p>
<p class="abs center intro-p" style="top:874px">Sodass Sie sich wieder <b>zu Hause fühlen</b>!</p>

<section class="abs focus" role="img" aria-label="Frau in grünem Blazer mit Holzkette, unscharfer Hintergrund"></section>
<div class="abs focus-frame"></div>
<h2 class="abs center focus-title">Der Mensch im Fokus</h2>
<p class="abs center focus-sub">Der Einrichtungsstil - so individuell wie Sie</p>
<p class="abs center focus-text">Jedes Interior Konzept wird in enger Zusammenarbeit mit den<br>Kunden erstellt um das persönliche Wohlbefinden zu garantieren.</p>
<a class="abs btn-light">Referenzen</a>

<h2 class="abs about-title">Lernen Sie mich kennen</h2>
<div class="abs photo photo-portrait" role="img" aria-label="Porträt der Designerin zwischen Pflanzen"></div>
<div class="abs photo photo-room" role="img" aria-label="Helle Wand mit Bild, Wandleuchte und Zimmerpflanzen"></div>
<h3 class="abs card-title" style="left:129px">Über mich</h3>
<p class="abs card-text" style="left:129px">Als gelernte Dekorateurin mit einem Abschluss in Fashion Design sowie Visual Merchandising sehe ich auf eine fundierte Ausbildung und mehrere Jahre Berufserfahrung zurück. Meine Designaffinität möchte ich auch bei Ihnen einsetzten, um Ihre persönliche Wohlfühloase zu schaffen.</p>
<h3 class="abs card-title" style="left:611px">Meine Arbeit</h3>
<p class="abs card-text" style="left:611px">Interior ist meine Leidenschaft. Home Styling, Home Staging, Dekorationen aber auch Interior Designs entwerfe und führe ich für Sie aus. Räume zu erschaffen und ihnen eine persönliche Note zu verleihen ist mein Ziel, dass ich gerne zusammen mit Ihnen realisieren möchte.</p>

<section class="abs cta"></section>
<h2 class="abs center cta-title">Sind Sie an einer Zusammenarbeit interessiert?</h2>
<p class="abs center cta-text">Gerne berate ich Sie persönlich und unverbindlich bei einem ersten Gespräch.<br>Einen Überblick über meine Konditionen erhalten Sie hier:</p>
<a class="abs btn-outline">Konditionen</a>

<footer class="abs footer"></footer>
<p class="abs center footer-line" style="top:2621px"><a>lena@raumklang-studio.ch</a><span class="sep">-</span>079 000 12 34<span class="sep">-</span>Lindenweg 5, 6000 Musterdorf</p>
<p class="abs center footer-line footer-links" style="top:2685px"><a>Impressum</a><a>Datenschutz</a><a>Cookie-Einstellungen</a></p>

<p class="abs center builder"><span class="builder-name">Baukasto</span>Das kannst du auch! Melde dich kostenlos an bei <a>https://baukasto.example/</a></p>

</body>
</html>
```